Zielgruppe
Wir verkaufen spezielle Teemischungen an Frauen, die schwanger werden möchten und sich gezielt ein Mädchen oder einen Jungen wünschen. Die Rezeptur unseres Tees, ist speziell auf den jeweiligen Wunsch abgestimmt. Wir verkaufen daher einen Sonnenwiese Tee und einen Bergquelle Tee.
Aufgabenstellung
Wir benötigen ein Etikett Design für den Sonnenwiese Tee. Wenn das Etikett fertig designed wurde, würden wir gerne anschließend ein Etikett für den Bergquelle Tee designen lassen. Das Design sollte klar, hochwertig und modern wirken. Es sollte erkennbar sein, dass der Tee speziell für Frauen mit einem Mädchenwunsch ist. Die Hintergrundfarbe des Designes bzw. des Etiketts sollte in zart rosa sein.

```html
<!DOCTYPE html>
<html lang="de">
<head>
<meta charset="utf-8">
<title>Sonnenwiese Tee – Etikett</title>
<link rel="stylesheet" href="https://fonts.googleapis.com/css2?family=Roboto:wght@300;400;500&display=swap">
<style>
  :root {
    --stage: #e2e2e2;
    --label-white: #fbfbfb;
    --brand-pink: #e0799b;
    --title-pink: #e2799c;
    --band-pink-a: #c9489e;
    --band-pink-b: #dc4a86;
    --bullet-dot: #ec9cbb;
    --weight-badge: #8ed2df;
    --weight-text: #3f8eac;
    --figure-a: #3f62c4;
    --figure-b: #3cc0e8;
    --text-light: #ffffff;
  }
  * { box-sizing: border-box; margin: 0; padding: 0; }
  html, body {
    width: 1200px; height: 964px; overflow: hidden;
    background: var(--stage);
    font-family: 'Roboto', sans-serif;
  }
  .label {
    position: absolute; left: 350px; top: 52px;
    width: 500px; height: 860px;
    background: var(--label-white);
    border-radius: 22px;
    overflow: hidden;
  }
  .brand {
    position: absolute; top: 150px; left: 0; width: 100%;
    display: flex; justify-content: center; align-items: center; gap: 14px;
  }
  .brand-dot {
    width: 22px; height: 22px; border-radius: 50%;
    background: var(--brand-pink);
  }
  .brand-name {
    font-weight: 300; font-size: 46px; letter-spacing: 2px;
    color: var(--brand-pink);
  }
  .title {
    position: absolute; top: 282px; width: 100%; text-align: center;
    font-weight: 500; font-size: 34px; color: var(--title-pink);
    letter-spacing: 0.3px;
  }
  .subtitle {
    position: absolute; top: 322px; width: 100%; text-align: center;
    font-weight: 500; font-size: 15.5px; color: var(--title-pink);
  }
  .band {
    position: absolute; left: 0; right: 0; top: 382px; bottom: 0;
    background: linear-gradient(160deg, var(--band-pink-a), var(--band-pink-b));
    clip-path: polygon(0 0, 100% 10%, 100% 100%, 0 100%);
  }
  .figure-area {
    position: absolute; left: 190px; top: 500px; width: 310px; height: 360px;
    border-radius: 180px 0 0 0;
    background: linear-gradient(200deg, var(--figure-a), var(--figure-b) 70%);
    opacity: 0.85;
  }
  .features {
    position: absolute; left: 62px; top: 448px;
    list-style: none;
  }
  .features li {
    display: flex; align-items: center; gap: 12px;
    height: 56px;
    font-size: 19.5px; font-weight: 400; color: var(--text-light);
  }
  .features li::before {
    content: ""; width: 34px; height: 34px; border-radius: 50%;
    background: var(--bullet-dot); flex: none;
  }
  .weight {
    position: absolute; left: 60px; top: 692px;
    width: 72px; height: 72px; border-radius: 50%;
    background: var(--weight-badge);
    display: flex; align-items: center; justify-content: center;
    font-weight: 500; font-size: 20px; color: var(--weight-text);
  }
</style>
</head>
<body>
  <main class="label">
    <div class="brand">
      <span class="brand-dot"></span>
      <span class="brand-name">Lunaro</span>
    </div>
    <h1 class="title">SONNENWIESE TEE</h1>
    <p class="subtitle">AUßERGEWÖHNLICHE KINDERWUNSCH REZEPTUR</p>
    <div class="band"></div>
    <div class="figure-area" role="img" aria-label="Illustration einer sitzenden schwangeren Frau im blauen Kleid"></div>
    <ul class="features">
      <li>AUS KONTROLLIERTEM ANBAU</li>
      <li>PREMIUM QUALITÄT</li>
      <li>ENTHÄLT MATCHA</li>
      <li>INKLUSIVE E-BOOK!</li>
    </ul>
    <div class="weight">75g</div>
  </main>
</body>
</html>
```